Design the World's Greatest Valentine's Day Greeting Card

We're looking for designers who can create the best Valentine's Day greeting card designs in the world. Your design could be could be extra special because it is funny, beautiful, inspiring or original.

Your designs should be able to fit on a standard 4"x6" greeting card. The main design will need to be for the front page (cover) of the card, but you can also include some design for the inside pages if you like.

Multiple winners will be awarded, and will be chosen within 5 days after the contest ends on February 13, 2019.
First Prize: $200
Runners-up: $100 each

The winning card design (or designs) could be recognised as standout designs publicly, as they can be used, by Gigmarten.com, at it sole discretion, in some Gigmarten.com marketing or PR materials.

Let's celebrate Valentine's Day together by showcasing your designs!

```html
<!DOCTYPE html>
<html lang="en">
<head>
<meta charset="utf-8">
<title>Happy Valentine's Day Card</title>
<link rel="stylesheet" href="https://fonts.googleapis.com/css2?family=Montserrat:wght@800&family=Libre+Baskerville:ital@1&display=swap">
<style>
  :root {
    --coral: #f6706e;
    --navy: #0d3450;
    --heart-light: #f49a8f;
    --heart-deep: #c9505a;
  }
  * { margin: 0; padding: 0; box-sizing: border-box; }
  html, body {
    width: 1200px;
    height: 852px;
    overflow: hidden;
    background: var(--coral);
  }
  .card {
    position: relative;
    width: 1200px;
    height: 852px;
    background: var(--coral);
    overflow: hidden;
  }
  .band {
    position: absolute;
    left: 0;
    width: 100%;
    background: var(--navy);
  }
  .band--top-outer { top: 0; height: 94px; }
  .band--top-inner { top: 116px; height: 50px; }
  .band--bottom-inner { top: 694px; height: 44px; }
  .band--bottom-outer { top: 758px; height: 94px; }

  .heart-art {
    position: absolute;
    left: 40px;
    top: 180px;
    width: 420px;
    height: 500px;
    border-radius: 46% 46% 50% 50% / 38% 38% 62% 62%;
    background: radial-gradient(ellipse at 50% 45%, var(--heart-light) 0%, var(--heart-deep) 70%, var(--coral) 100%);
  }

  .greeting {
    position: absolute;
    left: 477px;
    top: 250px;
    color: var(--navy);
  }
  .greeting__title {
    font-family: "Montserrat", sans-serif;
    font-weight: 800;
    font-size: 82px;
    line-height: 102px;
    letter-spacing: 5px;
    text-transform: uppercase;
  }
  .greeting__quote {
    margin-top: 26px;
    font-family: "Libre Baskerville", serif;
    font-style: italic;
    font-size: 33px;
    color: var(--navy);
    white-space: nowrap;
  }
</style>
</head>
<body>
  <main class="card">
    <div class="band band--top-outer"></div>
    <div class="band band--top-inner"></div>

    <div class="heart-art" role="img" aria-label="Engraved anatomical heart illustration with radiating lines"></div>

    <section class="greeting">
      <h1 class="greeting__title">Happy<br>Valentine's<br>Day</h1>
      <p class="greeting__quote">"Because you deserve a true heart"</p>
    </section>

    <div class="band band--bottom-inner"></div>
    <div class="band band--bottom-outer"></div>
  </main>
</body>
</html>
```